Torvane Systems*

Stationary design including business cards, letter heads, envelops and email signatures using our new logo

Target Market(s)

Innovative Technologies

Industry/Entity Type

Defense Contracting

Font styles to use
Sans Serif

```html
<!DOCTYPE html>
<html lang="en">
<head>
<meta charset="utf-8">
<title>Torvane Systems Letterhead</title>
<link href="https://fonts.googleapis.com/css2?family=Open+Sans:wght@400;600&family=Roboto:wght@400;500&display=swap" rel="stylesheet">
<style>
  :root {
    --backdrop: #dedede;
    --paper: #fbfbfb;
    --ink: #111111;
    --body-text: #4a4a4a;
    --footer-text: #3a3a3a;
    --band: #050607;
    --signature-tone: #cfcfcf;
  }
  * { margin: 0; padding: 0; box-sizing: border-box; }
  html, body { width: 1200px; height: 800px; overflow: hidden; }
  body { background: var(--backdrop); position: relative; }

  .letterhead {
    position: absolute;
    left: 327px; top: 20px;
    width: 545px; height: 760px;
    background: var(--paper);
    font-family: "Open Sans", sans-serif;
    color: var(--body-text);
  }
  .brand {
    position: absolute;
    top: 84px; left: 0; width: 100%;
    text-align: center;
    font-family: "Open Sans", sans-serif;
    font-weight: 600;
    font-size: 18px;
    letter-spacing: 0.5px;
    color: var(--ink);
  }
  .letter-body {
    position: absolute;
    left: 49px; top: 182px;
    width: 447px;
    font-size: 9.9px;
    line-height: 14.6px;
  }
  .salutation { margin-bottom: 15px; }
  .paragraph { text-align: justify; margin-bottom: 14.6px; }
  .closing { margin-top: 29px; }
  .signature {
    position: absolute;
    left: 49px; top: 520px;
    width: 66px; height: 60px;
    background: linear-gradient(135deg, var(--paper), var(--signature-tone), var(--paper));
    border-radius: 4px;
  }
  .contact {
    position: absolute;
    left: 49px; top: 690px;
    font-family: "Roboto", sans-serif;
    font-size: 10.3px;
    line-height: 13.4px;
    color: var(--footer-text);
  }
  .contact-line { display: flex; align-items: center; gap: 4px; }
  .contact-line svg { width: 9px; height: 9px; fill: var(--ink); }
  .address {
    position: absolute;
    right: 49px; top: 690px;
    text-align: right;
    font-family: "Roboto", sans-serif;
    font-size: 10.3px;
    line-height: 13.4px;
    color: var(--footer-text);
  }
  .address-name { font-weight: 500; color: var(--ink); }
  .footer-band {
    position: absolute;
    left: 0; bottom: 0;
    width: 100%; height: 13px;
    background: var(--band);
  }
</style>
</head>
<body>
  <main class="letterhead">
    <div class="brand">TORVANE SYSTEMS</div>

    <section class="letter-body">
      <p class="salutation">Dear customer,</p>
      <p class="paragraph">Lorem ipsum dolor sit amet, consectetur adipisicing elit, sed do eiusmod tempor incididunt ut labore et dolore magna aliqua. Ut enim ad minim veniam, quis nostrud exercitation ullamco laboris nisi ut aliquip ex ea commodo consequat. Duis aute irure dolor in reprehenderit in voluptate velit esse cillum dolore eu fugiat nulla pariatur. Excepteur sint occaecat cupidatat non proident, sunt in culpa qui officia deserunt mollit anim id est laborum.</p>
      <p class="paragraph">Lorem ipsum dolor sit amet, consectetur adipisicing elit, sed do eiusmod tempor incididunt ut labore et dolore magna aliqua. Ut enim ad minim veniam, quis nostrud exercitation ullamco laboris nisi ut aliquip ex ea commodo consequat. Duis aute irure dolor in reprehenderit in voluptate velit esse cillum dolore eu fugiat nulla pariatur. Excepteur sint occaecat cupidatat non proident, sunt in culpa qui officia deserunt mollit anim id est laborum.</p>
      <p class="paragraph">Lorem ipsum dolor sit amet, consectetur adipisicing elit, sed do eiusmod tempor incididunt ut labore et dolore magna aliqua. Ut enim ad minim veniam, quis nostrud exercitation ullamco laboris nisi ut aliquip ex ea commodo consequat. Duis aute irure dolor in reprehenderit in voluptate velit esse cillum dolore eu fugiat nulla pariatur. Excepteur sint occaecat cupidatat non proident, sunt in culpa qui officia deserunt mollit anim id est laborum.</p>
      <p class="closing">Yours Sincerely,</p>
    </section>

    <div class="signature" role="img" aria-label="Handwritten signature"></div>

    <div class="contact">
      <div class="contact-line">
        <svg viewBox="0 0 10 10" aria-hidden="true"><path d="M1 3.5C1 2 2.5 1.5 5 1.5S9 2 9 3.5L7.5 4 7 3H3L2.5 4zM2.5 4.5h5L8.5 8.5h-7z"/></svg>
        <span>555.014.2290</span>
      </div>
      <div class="contact-line">
        <svg viewBox="0 0 10 10" aria-hidden="true"><path d="M0.5 2h9v6h-9z M1 2.5l4 3 4-3" stroke="#fff" stroke-width="0.6"/></svg>
        <span>ana@torvanesystems.com</span>
      </div>
      <div class="contact-line">
        <svg viewBox="0 0 10 10" aria-hidden="true"><circle cx="5" cy="5" r="4.5"/><path d="M3 2.5c1 .5 1.5 1.5 1 2.5s1 1.5 1.5 3M6.5 2c-.5 1 .5 2 1.5 2" stroke="#fff" stroke-width="0.7" fill="none"/></svg>
        <span>www.torvanesystems.com</span>
      </div>
    </div>

    <div class="address">
      <div class="address-name">Torvane Systems</div>
      <div>4120 Ledger Point Road</div>
      <div>Fairbrook, Oh 45000</div>
    </div>

    <div class="footer-band"></div>
  </main>
</body>
</html>
```